Bar Soap Packaging Design for Facial Cleansing Bar

Hi,

I have a business that sells soaps, lotions, and other skincare products and I'd like a design for a box for a bar soap that is primarily for women.

The name of the brand is 'Velmo Shea Blend' and the brand is all about renewal and rejuvenation.

I've attached my logo and photos of packaging for bar soaps that are best sellers in my market.

The box is 3 inches x 2 inches and has a white background.

Info to go on the box:

1. Brand name: Velmo Shea Blend

2. [To go below brand name]: Facial Bar

3. Address: Distributed by Haverlin Trading Ltd, 47 Marlow St., Kingston, Jamaica W.I.

4. Contact: tamsin@velmosheablend.example

5. Net Weight: 3.6 oz /102g

6. Ingredients: glycerine, palmitic acid, sodium chloride, water, cocoa butter, fragrance, AOS, EDTA, vitamin E, color.

7. Directions: Wet face. Lather soap in hands. Gently massage lather onto face and neck. Rinse with water and pat dry with a towel. For day, follow with a sunscreen. At night, follow with a serum and/or moisturizer.

8. Please put a circle somewhere on the front with the words: 'Boosts Hydration 100%' in the circle

9. Batch Code: [please leave space beside 'Batch Code' blank]

10. Best Before: April 2019

11. Please put somewhere on the the front: For Younger Looking Skin

12. Please put somewhere on the front: with Real Cocoa Butter and Vitamin E

Thank you,
Tamsin

Target Market(s)

Women 27 to 60 who are looking for anti-age skincare products that'll make them look younger

Industry/Entity Type

Business

Font styles to use
Sans Serif

Colors

Designer to choose colors to be used in the design.

Requirements
Must have
• The info that I've asked for in the brief
Nice to have
• A design similar to the packaging for the brand of soap 'Odra' that I've attached.
Should not have
• Not sure...

```html
<!DOCTYPE html>
<html lang="en">
<head>
<meta charset="utf-8">
<title>Velmo Shea Blend – Facial Bar Box</title>
<link rel="stylesheet" href="https://fonts.googleapis.com/css2?family=Marcellus&family=Playball&family=Cinzel:wght@500&family=Mulish:wght@400&family=Roboto+Condensed:wght@400;700&display=swap">
<style>
  :root {
    --navy: #2c2e8e;
    --brown: #8a5c33;
    --brown-text: #6e4a28;
    --tan: #c99a6c;
    --beige-edge: #d9cbbd;
    --cream: #f3e9df;
    --grey-band: #d9d6d3;
    --ink: #222222;
    --sky: #3d9ad8;
    --white: #ffffff;
  }
  * { margin: 0; padding: 0; box-sizing: border-box; }
  html, body { width: 1200px; height: 1000px; overflow: hidden; background: var(--white); }
  .canvas { position: relative; width: 1200px; height: 1000px; }

  .panel {
    position: absolute; top: 336px; width: 535px; height: 355px;
    border: 2px solid var(--beige-edge);
    background: linear-gradient(to bottom, var(--cream) 0px, var(--white) 45px, var(--white) 300px, #ead9c7 335px, var(--tan) 355px);
    overflow: hidden;
  }
  .panel--back { left: 55px; }
  .panel--front { left: 617px; }
  .panel > * { position: absolute; }

  .brand-name {
    font-family: "Marcellus", serif; color: var(--navy);
    line-height: 1.05;
  }
  .product-title {
    font-family: "Playball", cursive; color: var(--navy); line-height: 1; white-space: nowrap;
  }
  .tagline {
    font-family: "Cinzel", serif; color: var(--brown-text); white-space: nowrap; letter-spacing: .02em;
  }
  .claim-pill {
    background: var(--brown); color: var(--white); border-radius: 10px;
    font-family: "Mulish", sans-serif; text-align: center; white-space: nowrap;
  }

  /* back panel */
  .panel--back .brand-name { left: 70px; top: 38px; font-size: 24px; width: 150px; }
  .panel--back .product-title { left: 228px; top: 40px; font-size: 62px; }
  .panel--back .tagline { left: 229px; top: 106px; font-size: 14px; }
  .panel--back .claim-pill { left: 112px; top: 140px; width: 270px; height: 19px; font-size: 12px; line-height: 19px; }
  .copy { font-family: "Roboto Condensed", sans-serif; font-size: 14.5px; line-height: 17px; color: var(--ink); left: 72px; width: 380px; }
  .copy strong { font-weight: 700; }
  .copy--ingredients { top: 176px; }
  .copy--directions { top: 216px; }
  .batch-box { left: 290px; top: 280px; width: 155px; height: 24px; border: 1px solid #dcc3a2; background: var(--white); }
  .best-before { left: 324px; top: 311px; font-family: "Roboto Condensed", sans-serif; font-size: 11px; color: var(--ink); }

  /* front panel */
  .panel--front .brand-name { left: 38px; top: 36px; font-size: 30px; width: 170px; }
  .panel--front .product-title { left: 200px; top: 90px; font-size: 82px; }
  .panel--front .tagline { left: 230px; top: 175px; font-size: 16px; }
  .panel--front .claim-pill { left: 218px; top: 204px; width: 268px; height: 19px; font-size: 12px; line-height: 19px; }
  .wave { left: 0; top: 0; width: 535px; height: 355px; }
  .hero-art {
    left: 40px; top: 132px; width: 150px; height: 150px; border-radius: 50%;
    background: radial-gradient(circle at 45% 40%, #f7e27a 0%, #f2d24a 35%, #a8623a 70%, rgba(220,230,240,0) 100%);
  }
  .badge {
    left: 315px; top: 240px; width: 66px; height: 66px; border-radius: 50%;
    background: var(--sky); border: 2px solid var(--sky); box-shadow: inset 0 0 0 2px var(--white);
    color: var(--white); font-family: "Roboto Condensed", sans-serif; text-align: center;
    display: flex; flex-direction: column; justify-content: center; line-height: 1.05;
  }
  .badge__small { font-size: 9px; text-transform: uppercase; }
  .badge__big { font-size: 16px; font-weight: 700; }
  .distributor { left: 30px; top: 297px; font-family: "Roboto Condensed", sans-serif; font-size: 9px; line-height: 10px; color: var(--ink); }
  .net-weight { left: 369px; top: 324px; font-family: "Roboto Condensed", sans-serif; font-size: 13px; color: var(--ink); }
</style>
</head>
<body>
<main class="canvas">

  <section class="panel panel--back" aria-label="Back of box">
    <p class="brand-name">Velmo Shea Blend</p>
    <h2 class="product-title">Facial Bar</h2>
    <p class="tagline">For Younger Looking Skin</p>
    <p class="claim-pill">with Real Cocoa Butter and Vitamin E</p>
    <p class="copy copy--ingredients"><strong>Ingredients:</strong> glycerine, palmitic acid, sodium chloride, water, cocoa butter, fragrance, AOS, EDTA, vitamin E, color.</p>
    <p class="copy copy--directions"><strong>Directions:</strong> Wet face. Lather soap in hands. Gently massage lather onto face and neck. Rinse with water and pat dry with a towel. For day, follow with a sunscreen. At night, follow with a serum and/or moisturizer.</p>
    <div class="batch-box" aria-label="Batch code space"></div>
    <p class="best-before">Best Before: April 2019</p>
  </section>

  <section class="panel panel--front" aria-label="Front of box">
    <svg class="wave" viewBox="0 0 535 355" aria-hidden="true">
      <path d="M0,232 C70,282 140,300 225,298 C330,296 420,262 535,262 L535,296 C420,296 330,312 225,312 C140,312 60,290 0,250 Z" fill="var(--grey-band)"/>
      <path d="M0,226 C70,272 140,292 225,290 C330,288 420,254 535,250 L535,270 C420,272 330,300 225,302 C140,304 60,280 0,240 Z" fill="var(--tan)"/>
    </svg>
    <p class="brand-name">Velmo Shea Blend</p>
    <h1 class="product-title">Facial Bar</h1>
    <p class="tagline">For Younger Looking Skin</p>
    <p class="claim-pill">with Real Cocoa Butter and Vitamin E</p>
    <div class="hero-art" role="img" aria-label="Yellow vanilla flower and cocoa bean resting in a milky water splash"></div>
    <div class="badge"><span class="badge__small">Boosts</span><span class="badge__small">Hydration</span><span class="badge__big">100%</span></div>
    <p class="distributor"><strong>Distributed by</strong><br>Haverlin Trading Ltd, 47 Marlow St.,<br>Kingston, Jamaica W.I.<br>Contact: tamsin@velmosheablend.example</p>
    <p class="net-weight">Net Weight: 3.6 oz /102g</p>
  </section>

</main>
</body>
</html>
```